Letterhead Design for Law Firm that Specializes in Property Damage Litigation

We are looking for a redesign of our letterhead. Our current letterhead lists all of our current staff members and we'd like to come up with a design that does NOT list all of the staff members so that it does not need to be updated with every newly hired employee. Must be in editable format.

We are a law firm that specializes in property damage, so we need something that is professional, yet modern. The final design should use our existing logo and should use a blue color scheme (alternate colors would be gray, black, and white).

Industry/Entity Type

Legal

Colors
0054AA
0677BA
7BADD7
CADEEF
E8F1F8

```html
<!DOCTYPE html>
<html lang="en">
<head>
<meta charset="utf-8">
<title>Harlow Mercer &amp; Vance — Letterhead</title>
<link href="https://fonts.googleapis.com/css2?family=Cinzel:wght@500&family=Open+Sans:wght@300;400;600&display=swap" rel="stylesheet">
<style>
  :root {
    --blue-deep: #0054AA;
    --blue-mid: #0677BA;
    --blue-soft: #7BADD7;
    --blue-pale: #CADEEF;
    --blue-mist: #E8F1F8;
    --ink: #1d1d1f;
    --gray-text: #6b6b6b;
    --gray-light: #c8c8c8;
    --gray-band: #b3b6b6;
    --label-bg: #ececec;
    --paper: #ffffff;
    --backdrop: #e6e7e7;
  }
  * { box-sizing: border-box; margin: 0; padding: 0; }
  html, body { width: 1200px; height: 984px; overflow: hidden; }
  body {
    background: var(--backdrop);
    font-family: "Open Sans", Arial, sans-serif;
    position: relative;
  }
  .letterhead {
    position: absolute;
    left: 252px; top: 40px;
    width: 696px; height: 904px;
    background: var(--paper);
    box-shadow: 0 6px 24px rgba(0,0,0,0.12);
    overflow: hidden;
  }
  .masthead { position: absolute; left: 52px; top: 52px; }
  .firm-name {
    display: flex; align-items: center; gap: 10px;
    font-family: "Cinzel", "Times New Roman", serif;
    font-weight: 500; font-size: 22px; letter-spacing: 0.5px;
    color: var(--gray-text); line-height: 1.05;
  }
  .firm-mark { width: 14px; height: 14px; background: var(--blue-deep); flex: none; }
  .firm-tagline {
    margin-top: 6px; margin-left: 24px;
    font-size: 10px; letter-spacing: 0.6px; text-transform: uppercase;
    color: var(--gray-text);
  }
  .footer-contact { position: absolute; left: 52px; bottom: 70px; }
  .main-phone { font-size: 24px; color: var(--ink); font-weight: 400; }
  .main-web { font-size: 26px; color: var(--gray-light); font-weight: 300; margin-top: -4px; }
  .main-rule { border-bottom: 2px dotted var(--gray-light); width: 640px; margin-top: 4px; }
  .offices {
    position: absolute; right: 40px; bottom: 110px;
    display: flex; gap: 30px;
  }
  .office-label {
    display: inline-block; background: var(--label-bg);
    font-family: "Cinzel", "Times New Roman", serif;
    font-size: 11px; color: var(--gray-text); padding: 2px 8px; margin-bottom: 6px;
  }
  .office-line {
    display: flex; align-items: flex-start; gap: 6px;
    font-size: 10px; color: var(--ink); line-height: 1.5;
  }
  .office-line svg { flex: none; margin-top: 3px; }
  .office-line.indent { padding-left: 15px; }
  .base-bands { position: absolute; left: 0; bottom: 0; width: 696px; height: 40px; }
</style>
</head>
<body>
  <main class="letterhead">
    <header class="masthead">
      <div class="firm-name"><span class="firm-mark"></span>Harlow Mercer &amp; Vance</div>
      <div class="firm-tagline">The Property Damage Attorneys</div>
    </header>

    <section class="offices">
      <div class="office">
        <div class="office-label">Fairview Office</div>
        <div class="office-line"><svg width="9" height="9"><circle cx="4.5" cy="4.5" r="4.5" fill="var(--blue-soft)"/></svg>555.204.3100</div>
        <div class="office-line"><svg width="9" height="9"><circle cx="4.5" cy="4.5" r="4.5" fill="var(--blue-soft)"/></svg>555.204.3101</div>
        <div class="office-line"><svg width="9" height="9"><circle cx="4.5" cy="4.5" r="4.5" fill="var(--blue-soft)"/></svg>2400 Market Row Suite 810</div>
        <div class="office-line indent">Fairview, PA 19000</div>
      </div>
      <div class="office">
        <div class="office-label">Brookdale Office</div>
        <div class="office-line"><svg width="9" height="9"><circle cx="4.5" cy="4.5" r="4.5" fill="var(--blue-soft)"/></svg>555.318.2200</div>
        <div class="office-line"><svg width="9" height="9"><circle cx="4.5" cy="4.5" r="4.5" fill="var(--blue-soft)"/></svg>555.204.3101</div>
        <div class="office-line"><svg width="9" height="9"><circle cx="4.5" cy="4.5" r="4.5" fill="var(--blue-soft)"/></svg>118 Linden Avenue, Suite 305</div>
        <div class="office-line indent">Brookdale, NJ 08000</div>
      </div>
    </section>

    <section class="footer-contact">
      <div class="main-phone">(555) 204-3100</div>
      <div class="main-web">www.hmvlegal.com</div>
      <div class="main-rule"></div>
    </section>

    <svg class="base-bands" viewBox="0 0 696 40" aria-hidden="true">
      <polygon points="0,12 430,12 410,40 0,40" fill="var(--blue-pale)"/>
      <polygon points="430,0 696,0 696,40 410,40" fill="var(--gray-band)"/>
    </svg>
  </main>
</body>
</html>
```